UK Online Escort Directory Requires a Redesigned Email Marketing Campaign (4 emails total)

These emails should be designed as marketing emails that will be sent out to approx 10,000 potential customers on a by monthly basis. The designs should be innovative, professional designs that are capable of capturing a readers attention in the blink of an eye.

We have posted this job as our in-house design capabilities are not able to create professional email designs, we therefore require a designer to redesign our email marketing campaign (4 emails total) to a professional level.

The content of the emails will be provided, along with the 5 emails that we are currently sending and the company logo. This should give the potential designer all that they need to redesign the campaign to a professional level.

Please see attached brief for more information on what is required from each individual email.

Target Market(s)

Escorts throughout the UK

Industry/Entity Type

Escort

Font styles to use
Serif
Sans Serif

Requirements
Must have
• Instant recognition of what's being offered.
Nice to have
• Imaginative / inspirational designs.
Should not have
• Any unnecessary wording or text.

```html
<!DOCTYPE html>
<html lang="en">
<head>
<meta charset="utf-8">
<title>Weekly Ad Performance Email</title>
<link rel="stylesheet" href="https://fonts.googleapis.com/css2?family=Oswald:wght@400;500&family=Open+Sans:wght@400;600&display=swap">
<style>
  :root {
    --rose: #d9737a;
    --panel: #efefef;
    --white: #ffffff;
    --ink: #111111;
    --body-grey: #666666;
    --muted: #8a8a8a;
    --gold: #fbc300;
    --plum: #a0226e;
    --brand: #d48aa8;
    --tagline: #4a6fb5;
    --rule: #c9c9c9;
  }
  * { box-sizing: border-box; margin: 0; padding: 0; }
  html, body { width: 1014px; height: 1200px; overflow: hidden; background: var(--white); }
  .email {
    width: 600px; height: 710px;
    transform: scale(1.69); transform-origin: 0 0;
    position: relative; background: var(--panel);
    font-family: "Open Sans", Arial, sans-serif; color: var(--ink);
  }
  .masthead { position: absolute; left: 0; top: 0; width: 600px; height: 118px; background: var(--white); }
  .brand-name {
    position: absolute; left: 22px; top: 22px;
    font-family: "Open Sans", Arial, sans-serif; font-weight: 400;
    font-size: 44px; letter-spacing: -0.5px; color: var(--brand); line-height: 1;
  }
  .tagline {
    position: absolute; left: 26px; top: 80px;
    font-weight: 600; font-size: 13px; color: var(--tagline);
  }
  .headline-band {
    position: absolute; left: 0; top: 118px; width: 600px; height: 37px;
    background: var(--rose); color: var(--white);
    font-family: "Oswald", sans-serif; font-size: 18px; text-align: center; line-height: 37px;
    text-transform: uppercase; letter-spacing: 0.3px;
  }
  .band-notch { position: absolute; left: 264px; top: 154px; width: 72px; height: 28px; }
  .stats {
    position: absolute; left: 0; top: 166px; width: 600px; text-align: center;
    font-size: 17px; white-space: nowrap;
  }
  .stats .figure { font-family: "Oswald", sans-serif; font-size: 48px; font-weight: 500; vertical-align: -4px; margin: 0 2px; }
  .price-pill {
    position: absolute; left: 187px; top: 245px; width: 225px; height: 53px;
    background: var(--gold); border-radius: 27px; text-align: center; line-height: 53px;
    font-size: 16px;
  }
  .price-pill .amount { font-family: "Oswald", sans-serif; font-size: 30px; font-weight: 500; vertical-align: -2px; }
  .listing-card {
    position: absolute; left: 23px; top: 330px; width: 555px; height: 210px; background: var(--white);
  }
  .listing-photo {
    position: absolute; left: 15px; top: 15px; width: 121px; height: 180px;
    background: linear-gradient(160deg, #d8b07a 0%, #b98a6a 45%, #5a3f35 100%);
  }
  .premium-badge {
    position: absolute; right: 15px; top: 16px; width: 91px; height: 28px;
    border: 1px solid var(--plum); color: var(--plum); font-size: 14px; text-align: center; line-height: 26px;
  }
  .listing-name { position: absolute; left: 151px; top: 42px; font-size: 18px; font-weight: 600; }
  .listing-location { position: absolute; left: 151px; top: 65px; font-size: 14px; }
  .listing-text {
    position: absolute; left: 151px; top: 97px; width: 380px;
    font-size: 14px; line-height: 24.5px; color: var(--body-grey);
  }
  .card-rule { position: absolute; left: 23px; top: 540px; width: 555px; height: 5px; border-top: 1px solid var(--rule); border-bottom: 1px solid var(--rule); }
  .cta { position: absolute; top: 576px; text-align: center; }
  .cta-left { left: 0; width: 308px; }
  .cta-right { left: 296px; width: 300px; }
  .cta-button {
    display: inline-block; background: var(--ink); color: var(--white);
    font-size: 14px; height: 33px; line-height: 33px; padding: 0 18px;
  }
  .cta-url { margin-top: 11px; font-size: 14px; color: var(--ink); }
  .footer {
    position: absolute; left: 0; top: 660px; width: 600px; height: 50px; background: var(--white);
    text-align: center; line-height: 50px; font-size: 12px; color: var(--muted);
  }
</style>
</head>
<body>
<main class="email">
  <header class="masthead">
    <div class="brand-name">velvetdirectory-uk.com</div>
    <div class="tagline">The Escort Directory</div>
  </header>

  <div class="headline-band">Last week this ad was</div>
  <svg class="band-notch" viewBox="0 0 72 28" aria-hidden="true">
    <path d="M0 0 H72 C52 0 40 10 36 28 C32 10 20 0 0 0 Z" fill="var(--rose)"/>
  </svg>

  <p class="stats">viewed <span class="figure">963</span> times and produced <span class="figure">150</span> phone calls</p>

  <div class="price-pill">for just <span class="amount">£40.49</span>pm</div>

  <article class="listing-card">
    <div class="listing-photo" role="img" aria-label="Profile photo of the advertiser"></div>
    <div class="premium-badge">Premium</div>
    <h2 class="listing-name">Lena,22</h2>
    <p class="listing-location">Birmingham City Centre Escort</p>
    <p class="listing-text">New to Birmingham - Hello Guys, my name is Lena, I am from Sweden. My pictures are 100% genuine, I am a glamour model. Call me Kisses Lena xxx xxx I look forward to meeting you x</p>
  </article>
  <div class="card-rule"></div>

  <div class="cta cta-left">
    <span class="cta-button">Take a look@</span>
    <p class="cta-url">www.velvetdirectory-uk.com/</p>
  </div>
  <div class="cta cta-right">
    <span class="cta-button">Post an add@</span>
    <p class="cta-url">www.velvetdirectory-uk.com/post/add/</p>
  </div>

  <footer class="footer">Copyright 2016 Velvetdirectory-uk.com All Rights Reserved</footer>
</main>
</body>
</html>
```